VeloNest Crowdfunding Website 1st Page

I am looking to have a first page created for a new crowd funding website that knocks down the biggest hurdle that creative types and start ups face, legal costs. For creative projects and innovative products, we are providing intellectual property and certain other legal services wrapped into the project costs.

I am using a white label crowdfunding platform that that has a standard look and feel of most crowdfunding sites e.g. tiles with campaigns, listing of campaigns categories, create new campaign options, and donate to campaigns etc. The white label program is branded with the VeloNest logo and colors. At present there is a front page that is just a place holder for someone at ArtHive's great design! What I need is an eye-catching first page that visually and through content optimizes the VeloNest brand. (There should be space for content for those looking to raise money and those looking to donate to campaigns.)

www.pledgewave.example is, of course, the reigning King of crowdfunding. They have been so successful that they no longer have to entice people to launch campaigns there. (So they don't speak as much to those looking to raise money.) Unlike Pledgewave, of the challenges is that I have two customers I need to engage. The first is the potential crowdfund campaign owner who is looking to raise money. The second customer is the donor.

I am looking for a smart page from a marketing standpoint that also grabs you. One should feel the energy of "the crowd" when they look at the page.

Some information regarding the logo: The font is Kabel BK BT. The primary blue is R33, G121, B 159. Hex21799F and the primary greenis R179, G210, B54 Hex B3D236. The third file is a slight variation on the VN logo that you are free to use as well. (Unfortunately, I don't have all the color information for that one readily available.) If you need more files, please just let me know.

Industry/Entity Type

Marketing

Font styles to use
Other font styles liked:
• Kabel Bk BT or complimentary

Requirements
Must have
• Please use the slogan "Where the crowd meets great ideas".

```html
<!DOCTYPE html>
<html lang="en">
<head>
<meta charset="utf-8">
<title>VeloNest – Where the crowd meets great ideas</title>
<link href="https://fonts.googleapis.com/css2?family=Source+Sans+3:wght@400;600&family=Arimo:wght@400;700&display=swap" rel="stylesheet">
<style>
  :root {
    --brand-blue: #21799f;
    --brand-green: #b3d236;
    --hero-blue: #4f93b6;
    --hero-deep: #2f6e92;
    --ink: #1a1a1a;
    --body-ink: #333;
    --panel: #e8f0f5;
    --rule: #c9c9c9;
    --white: #fff;
  }
  * { margin: 0; padding: 0; box-sizing: border-box; }
  html, body { width: 1200px; height: 1178px; overflow: hidden; background: var(--white); }
  body { position: relative; font-family: "Source Sans 3", "Myriad Pro", sans-serif; color: var(--ink); }

  .site-header { position: absolute; top: 0; left: 0; width: 1200px; height: 70px; background: var(--white); }
  .brand { position: absolute; left: 211px; top: 13px; display: flex; align-items: center; gap: 9px; }
  .brand-dot { width: 47px; height: 47px; border-radius: 50%; background: var(--brand-blue); }
  .brand-name { font-size: 25px; font-weight: 400; color: var(--brand-blue); }
  .main-nav { position: absolute; left: 453px; top: 27px; display: flex; gap: 21px; font-size: 15px; }
  .main-nav a { color: var(--ink); text-decoration: none; }
  .main-nav .account { margin-left: 1px; color: var(--brand-green); }

  .hero { position: absolute; top: 70px; left: 0; width: 1200px; height: 401px;
    background: linear-gradient(100deg, var(--hero-deep) 0%, var(--hero-blue) 40%, #6aa6c4 75%, #4f8db0 100%); }
  .hero-title { position: absolute; left: 352px; top: 199px; font-size: 41px; line-height: 41px; font-weight: 400; color: var(--white); }
  .hero-actions { position: absolute; left: 352px; top: 301px; display: flex; gap: 21px; }
  .cta { display: block; width: 181px; height: 32px; line-height: 31px; text-align: center;
    background: var(--brand-green); color: var(--ink); font-size: 15px; text-decoration: none; }

  .carousel-arrow { position: absolute; top: 512px; width: 32px; height: 48px; }
  .carousel-arrow.prev { left: 119px; }
  .carousel-arrow.next { left: 1046px; }

  .project-card { position: absolute; top: 435px; width: 189px; height: 192px; background: var(--white);
    padding: 16px; box-shadow: 0 6px 10px rgba(0,0,0,.04); font-family: "Arimo", Arial, sans-serif; }
  .card-media { width: 156px; height: 90px; }
  .card-title { margin-top: 10px; font-size: 14px; font-weight: 700; color: var(--ink); padding-bottom: 10px; border-bottom: 1px solid var(--rule); }
  .project-card.active .card-title { border-bottom: 2px solid var(--brand-green); }
  .card-text { margin-top: 11px; font-size: 9.5px; line-height: 14px; color: var(--body-ink); }

  .featured-title { position: absolute; top: 645px; left: 0; width: 1200px; text-align: center;
    font-size: 33px; font-weight: 600; color: var(--brand-blue); }
  .featured-lead { position: absolute; top: 690px; left: 0; width: 1200px; text-align: center; font-size: 19.5px; color: var(--ink); }

  .featured-panel { position: absolute; top: 740px; left: 197px; width: 813px; height: 327px; background: var(--panel); }
  .feature { position: absolute; width: 355px; }
  .feature h3 { font-size: 20px; font-weight: 400; color: var(--ink); }
  .feature h3 strong { font-family: "Arimo", Arial, sans-serif; font-weight: 700; font-size: 19px; }
  .feature p { margin-top: 12px; font-size: 11.6px; line-height: 17px; color: var(--ink); }

  .site-footer { position: absolute; top: 1121px; left: 197px; width: 806px; border-top: 2px solid var(--brand-blue);
    padding-top: 16px; font-family: "Arimo", Arial, sans-serif; font-size: 9.5px; color: var(--body-ink); }
  .site-footer .brand-link { color: var(--brand-blue); }
</style>
</head>
<body>
  <header class="site-header">
    <div class="brand"><span class="brand-dot"></span><span class="brand-name">VeloNest</span></div>
    <nav class="main-nav">
      <a href="#">Start My Project</a>
      <a href="#">Find A Project</a>
      <a href="#">Community Wishlist</a>
      <a href="#">Blog</a>
      <a href="#" class="account">Register | Log In</a>
    </nav>
  </header>

  <section class="hero" role="img" aria-label="Blue-toned photo of three colleagues smiling around a desk in a bright office">
    <h1 class="hero-title">Where the crowd meets<br>great ideas</h1>
    <div class="hero-actions">
      <a class="cta" href="#">Looking to raise money</a>
      <a class="cta" href="#">Looking to donate</a>
    </div>
  </section>

  <svg class="carousel-arrow prev" viewBox="0 0 32 48" aria-label="Previous">
    <polygon points="24,0 32,6 14,24 32,42 24,48 0,24" fill="#b3d236"/>
    <polygon points="14,24 32,42 24,48 4,28" fill="#8fae1c"/>
  </svg>
  <svg class="carousel-arrow next" viewBox="0 0 32 48" aria-label="Next">
    <polygon points="8,0 0,6 18,24 0,42 8,48 32,24" fill="#b3d236"/>
    <polygon points="18,24 0,42 8,48 28,28" fill="#8fae1c"/>
  </svg>

  <article class="project-card active" style="left:197px">
    <div class="card-media" role="img" aria-label="Photo of a woman using a tablet on a sofa" style="background:linear-gradient(135deg,#6b5a4e,#a08a72 60%,#c58a3a)"></div>
    <h2 class="card-title">Lorem ipsum</h2>
    <p class="card-text">Lorem ipsum dolor sit amet,<br>omnis euismod indoctum mel.</p>
  </article>
  <article class="project-card" style="left:403px">
    <div class="card-media" role="img" aria-label="Photo of a man on the phone sitting on steps" style="background:linear-gradient(120deg,#c9c27a,#8a8a7a 45%,#2a2a2a)"></div>
    <h2 class="card-title">Lorem ipsum</h2>
    <p class="card-text">Lorem ipsum dolor sit amet,<br>omnis euismod indoctum mel.</p>
  </article>
  <article class="project-card" style="left:609px">
    <div class="card-media" role="img" aria-label="Photo of finger puppets with colourful speech bubbles" style="background:linear-gradient(180deg,#ededed,#e4d2c0 70%,#d8b79a)"></div>
    <h2 class="card-title">Lorem ipsum</h2>
    <p class="card-text">Lorem ipsum dolor sit amet,<br>omnis euismod indoctum mel.</p>
  </article>
  <article class="project-card" style="left:815px">
    <div class="card-media" role="img" aria-label="Image of dark interface buttons and toggles" style="background:linear-gradient(180deg,#3a3a3a,#222)"></div>
    <h2 class="card-title">Lorem ipsum</h2>
    <p class="card-text">Lorem ipsum dolor sit amet,<br>omnis euismod indoctum mel.</p>
  </article>

  <h2 class="featured-title">Featured Projects</h2>
  <p class="featured-lead">Lorem ipsum dolor sit amet, consectetur adipiscing elit. Donec facilisis diam massa</p>

  <section class="featured-panel">
    <div class="feature" style="left:32px;top:35px">
      <h3><strong>Lorem.</strong> ipsum dolor sit</h3>
      <p>Lorem ipsum dolor sit amet, consectetur adipiscing elit. Mauris interdum velit vitae nulla molestie eu commodo nulla dapibus. Donec id sollicitudin urna. Integer at dui ac leo fermentum varius eleifend ut libero. Mauris interdum velit vitae nulla molestie eu commodo nulla .</p>
    </div>
    <div class="feature" style="left:437px;top:35px">
      <h3><strong>Lorem.</strong> ipsum dolor sit</h3>
      <p>Lorem ipsum dolor sit amet, consectetur adipiscing elit. Mauris interdum velit vitae nulla molestie eu commodo nulla dapibus. Donec id sollicitudin urna. Integer at dui ac leo fermentum varius eleifend ut libero. Mauris interdum velit vitae nulla molestie eu commodo nulla .</p>
    </div>
    <div class="feature" style="left:32px;top:182px">
      <h3><strong>Lorem.</strong> ipsum dolor sit</h3>
      <p>Lorem ipsum dolor sit amet, consectetur adipiscing elit. Mauris interdum velit vitae nulla molestie eu commodo nulla dapibus. Donec id sollicitudin urna. Integer at dui ac leo fermentum varius eleifend ut libero. Mauris interdum velit vitae nulla molestie eu commodo nulla .</p>
    </div>
    <div class="feature" style="left:437px;top:182px">
      <h3><strong>Lorem.</strong> ipsum dolor sit</h3>
      <p>Lorem ipsum dolor sit amet, consectetur adipiscing elit. Mauris interdum velit vitae nulla molestie eu commodo nulla dapibus. Donec id sollicitudin urna. Integer at dui ac leo fermentum varius eleifend ut libero. Mauris interdum velit vitae nulla molestie eu commodo nulla .</p>
    </div>
  </section>

  <footer class="site-footer">©&nbsp; 2013 &nbsp;<span class="brand-link">VeloNest.</span> All Rights Reserved.</footer>
</body>
</html>
```